Real Estate Agent Business Card Needs a New Eye Catching Design

Looking for a designer that can revamp a current business card.
Looking for something with a lot more style.
Something that will catch the eye

Included in the file:
The old business card. (Old Business Card)
A new place holder image to be used as headshot. (Temp Headshot)
Homevane KT Logo (KT logo)
Fair Dwelling Access Logo (AC logo)

The working PSD file will need to be delivered with the individual layers separated and edible. (I'll being changing the new headshot later)
Any fonts used also need to be delivered.

Overall, the old business card has the elements but in a horrible state.
If you have any questions, please feel free to reach out.

Thank you

Glen

Target Market(s)

Individuals want to either sale or buy a home

Industry/Entity Type

Real Estate Agent

Design Requirements:
Headshot needs to be a head and shoulders and have a transparent background.

The American Flag should implemented into the design somehow.

Both the KT logo and AC logo need to be incorporated.

All information on the OLD Business Card should be included.

Requirements
Must have
• Transparent head shot set against the final background
• American Flag and/or colors-theme incorporated
• KT logo and AC logo incorporated

```html
<!DOCTYPE html>
<html lang="en">
<head>
<meta charset="UTF-8">
<title>Homevane Agent Business Card</title>
<link href="https://fonts.googleapis.com/css2?family=Open+Sans:wght@400;600;700;800&display=swap" rel="stylesheet">
<style>
  :root {
    --backdrop: #2b2b2b;
    --card-white: #ffffff;
    --flag-red: #c11f2f;
    --flag-blue: #2446a6;
    --ink: #161616;
    --photo-light: #e9c27f;
    --photo-dark: #b98a4a;
  }
  * { margin: 0; padding: 0; box-sizing: border-box; }
  html, body {
    width: 1200px; height: 900px; overflow: hidden;
    background: var(--backdrop);
    font-family: "Open Sans", sans-serif;
  }
  .card {
    position: absolute; left: 100px; top: 164px;
    width: 1000px; height: 571px;
    background: var(--card-white);
    overflow: hidden;
  }
  .card-art { position: absolute; inset: 0; }
  .brand-mark {
    position: absolute; left: 72px; top: 110px;
    display: flex; align-items: center; gap: 18px;
  }
  .brand-mark__square { width: 56px; height: 56px; background: var(--ink); }
  .brand-mark__name {
    font-weight: 800; font-size: 46px; color: var(--ink); letter-spacing: -0.5px;
  }
  .agent { position: absolute; left: 72px; top: 286px; color: var(--ink); }
  .agent__company { font-weight: 700; font-size: 36px; line-height: 1.2; }
  .agent__name { font-weight: 400; font-size: 29px; line-height: 1.25; margin-top: 2px; }
  .agent__title { font-weight: 400; font-size: 22px; line-height: 1.3; }
  .fair-housing {
    position: absolute; left: 112px; top: 452px;
    display: flex; flex-direction: column; align-items: center; gap: 8px;
  }
  .fair-housing__square { width: 64px; height: 64px; background: var(--ink); }
  .fair-housing__name {
    font-weight: 700; font-size: 12px; letter-spacing: 0.6px;
    text-transform: uppercase; color: var(--ink);
  }
  .headshot {
    position: absolute; left: 680px; top: 44px;
    width: 289px; height: 289px;
    background: linear-gradient(160deg, var(--photo-light), var(--photo-dark));
    box-shadow: 4px 5px 10px rgba(0,0,0,0.45);
  }
  .contact {
    position: absolute; left: 522px; top: 356px;
    list-style: none; color: #fff;
    font-size: 27px; line-height: 38px;
  }
  .contact__item { display: flex; align-items: flex-start; gap: 12px; }
  .contact__icon { width: 22px; height: 22px; margin-top: 8px; flex: none; fill: #fff; }
</style>
</head>
<body>
  <div class="card">
    <svg class="card-art" viewBox="0 0 1000 571" aria-hidden="true">
      <path fill="var(--flag-red)" d="M790 0 C700 120 570 240 500 305 C430 370 360 470 330 571 L1000 571 L1000 0 Z"/>
      <g fill="none">
        <path stroke="var(--flag-red)" stroke-width="10" d="M740 0 C650 120 520 240 450 305 C380 370 310 470 280 571"/>
        <path stroke="var(--flag-blue)" stroke-width="26" d="M770 0 C680 120 550 240 480 305 C410 370 340 470 310 571"/>
      </g>
      <g fill="#fff">
        <polygon points="774,8 777,16 785,16 779,21 781,29 774,24 767,29 769,21 763,16 771,16"/>
        <polygon points="735,64 738,72 746,72 740,77 742,85 735,80 728,85 730,77 724,72 732,72"/>
        <polygon points="690,122 693,130 701,130 695,135 697,143 690,138 683,143 685,135 679,130 687,130"/>
        <polygon points="642,176 645,184 653,184 647,189 649,197 642,192 635,197 637,189 631,184 639,184"/>
        <polygon points="590,230 593,238 601,238 595,243 597,251 590,246 583,251 585,243 579,238 587,238"/>
        <polygon points="532,284 535,292 543,292 537,297 539,305 532,300 525,305 527,297 521,292 529,292"/>
        <polygon points="472,338 475,346 483,346 477,351 479,359 472,354 465,359 467,351 461,346 469,346"/>
        <polygon points="418,400 421,408 429,408 423,413 425,421 418,416 411,421 413,413 407,408 415,408"/>
        <polygon points="372,464 375,472 383,472 377,477 379,485 372,480 365,485 367,477 361,472 369,472"/>
        <polygon points="336,530 339,538 347,538 341,543 343,551 336,546 329,551 331,543 325,538 333,538"/>
      </g>
    </svg>

    <div class="brand-mark">
      <span class="brand-mark__square"></span>
      <span class="brand-mark__name">Homevane KT</span>
    </div>

    <div class="agent">
      <p class="agent__company">Summit Star Realty</p>
      <p class="agent__name">Dana Holloway</p>
      <p class="agent__title">Homevane</p>
    </div>

    <div class="fair-housing">
      <span class="fair-housing__square"></span>
      <span class="fair-housing__name">Fair Dwelling Access</span>
    </div>

    <div class="headshot" role="img" aria-label="Head and shoulders portrait of the agent"></div>

    <ul class="contact">
      <li class="contact__item">
        <svg class="contact__icon" viewBox="0 0 24 24"><path d="M7 2h5l1 5-3 2a12 12 0 0 0 5 5l2-3 5 1v5c0 1-1 2-2 2A18 18 0 0 1 5 4c0-1 1-2 2-2z"/></svg>
        <span>555-014-2281</span>
      </li>
      <li class="contact__item">
        <svg class="contact__icon" viewBox="0 0 24 24"><path d="M6 2h12v6H6z M3 9h18v9h-3v-4H6v4H3z M7 15h10v7H7z"/></svg>
        <span>555-014-2290</span>
      </li>
      <li class="contact__item">
        <svg class="contact__icon" viewBox="0 0 24 24"><path d="M2 5h20v14H2z" /><path d="M2 5l10 8 10-8" fill="none" stroke="var(--flag-red)" stroke-width="2"/></svg>
        <span>dana.holloway@example.com</span>
      </li>
      <li class="contact__item">
        <svg class="contact__icon" viewBox="0 0 24 24"><path d="M12 2l11 10h-3v10h-6v-6h-4v6H4V12H1z"/></svg>
        <span>2217 s. Ridgeline Road Calder,<br>NV 89990</span>
      </li>
    </ul>
  </div>
</body>
</html>
```